Minimalist theatrical poster for the film

Create a poster, using some of the attached images for inspiration. Please match the font of the teaser poster for the title (The Bluewater) and leave space at the bottom for the credits block, which I will add later. Any characters presented on the poster should resemble the actors in the film, and not be clip art. The movie is about Owen, a 14 year old in the summer of 2001, and his first love (Greta). As he falls for her, he lets himself still be distracted by his good friend Maisie, eventually causing trouble in his relationships with Greta, Maisie, and best friend Theo. Trailer is included in the files below! Extra credit for a good marketing tag along the lines of "remember your first love" or something about the film being a romantic comedy adventure etc.

```html
<!DOCTYPE html>
<html lang="en">
<head>
<meta charset="utf-8">
<title>Owen &amp; The Bluewater — Poster</title>
<link rel="stylesheet" href="https://fonts.googleapis.com/css2?family=Mr+Dafoe&family=Sacramento&family=Oswald:wght@300;400&display=swap">
<style>
  :root {
    --backdrop: #333333;
    --mauve: #b46d98;
    --mauve-light: #e4c3da;
    --ink: #1c1a1c;
    --white: #ffffff;
    --cream: #fbf6ea;
  }
  * { margin: 0; padding: 0; box-sizing: border-box; }
  html, body { width: 1200px; height: 1200px; overflow: hidden; background: var(--backdrop); }
  .poster {
    position: absolute; left: 197px; top: 34px; width: 806px; height: 1132px;
    background: var(--mauve-light); overflow: hidden;
    box-shadow: 0 4px 18px rgba(0,0,0,.45);
  }
  .key-art {
    position: absolute; left: 0; top: 0; width: 806px; height: 776px;
    background:
      radial-gradient(ellipse 260px 200px at 200px 80px, var(--cream) 0%, rgba(251,246,234,0) 100%),
      radial-gradient(ellipse 260px 240px at 560px 280px, rgba(222,170,160,.9) 0%, rgba(222,170,160,0) 100%),
      radial-gradient(ellipse 220px 300px at 720px 560px, rgba(152,166,200,.95) 0%, rgba(152,166,200,0) 100%),
      radial-gradient(ellipse 120px 160px at 470px 640px, rgba(169,192,142,.9) 0%, rgba(169,192,142,0) 100%),
      radial-gradient(ellipse 300px 260px at 200px 520px, rgba(233,201,196,.95) 0%, rgba(233,201,196,0) 100%),
      radial-gradient(ellipse 200px 200px at 760px 120px, rgba(190,200,160,.7) 0%, rgba(190,200,160,0) 100%),
      linear-gradient(160deg, #f6ecdc 0%, #ead3cc 50%, #dcc3c8 100%);
  }
  .tag-box {
    position: absolute; left: 561px; top: 52px; width: 245px; height: 44px;
    background: var(--mauve); color: var(--white);
    font: 300 30px/44px "Oswald", sans-serif; padding-left: 13px; letter-spacing: .3px;
  }
  .tag-script {
    position: absolute; left: 545px; top: 98px; width: 240px; text-align: center;
    font: 400 74px/1 "Sacramento", cursive; color: var(--mauve);
  }
  .title-block { position: absolute; left: 0; top: 0; width: 806px; height: 776px; font-weight: 400; }
  .title { color: var(--white); font-family: "Mr Dafoe", cursive; position: absolute; white-space: nowrap;
    line-height: 1; text-shadow: 2px 3px 6px rgba(80,50,60,.35); }
  .title-owen { left: 40px; top: 170px; font-size: 200px; }
  .title-amp { left: 322px; top: 385px; font-size: 70px; }
  .title-the { left: 160px; top: 515px; font-size: 92px; }
  .title-main { left: 295px; top: 462px; font-size: 118px; }
  .rule { position: absolute; left: 0; width: 806px; height: 3px; background: var(--mauve); top: 777px; }
  .genre-band {
    position: absolute; left: 0; top: 783px; width: 806px; height: 47px;
    background: var(--mauve); color: var(--white); text-align: center;
    font: 300 29px/47px "Oswald", sans-serif; letter-spacing: .2px;
  }
  .stills { position: absolute; top: 832px; left: 0; width: 806px; height: 137px; display: flex; gap: 2px; }
  .still { height: 100%; }
  .still-park { width: 234px; background: linear-gradient(180deg, #6f8a4a 0%, #9fae80 45%, #b8aa90 70%, #9d8d76 100%); }
  .still-bowling { width: 330px; background: linear-gradient(180deg, #4a5a5c 0%, #2f3639 50%, #3c3a3c 100%); }
  .still-bikes { width: 238px; background: linear-gradient(180deg, #9a8a5a 0%, #a8a69a 40%, #8d8c88 100%); }
  .credits {
    position: absolute; top: 969px; left: 0; width: 806px; height: 163px;
    background: var(--mauve-light); color: var(--ink); text-align: center;
    font-family: "Oswald", sans-serif; font-weight: 300;
  }
  .credits p { font-size: 21px; line-height: 1; position: absolute; left: 0; width: 100%; }
  .credits small { font-size: 13px; }
  .credit-line-1 { top: 73px; }
  .credit-line-2 { top: 103px; }
  .credit-line-3 { top: 131px; }
</style>
</head>
<body>
  <main class="poster">
    <div class="key-art" role="img" aria-label="Soft-focus photo of two young teens leaning close in warm summer light"></div>

    <div class="tag-box">REMEMBER YOUR</div>
    <div class="tag-script">first love</div>

    <h1 class="title-block" aria-label="Owen &amp; The Bluewater">
      <span class="title title-owen">Owen</span>
      <span class="title title-amp">&amp;</span>
      <span class="title title-the">The</span>
      <span class="title title-main">Bluewater</span>
    </h1>

    <div class="rule"></div>
    <div class="genre-band">A ROMANTIC COMEDY WITH A SENSE OF ADVENTURE</div>

    <section class="stills">
      <div class="still still-park" role="img" aria-label="Film still: two friends on swings in a park"></div>
      <div class="still still-bowling" role="img" aria-label="Film still: four teens talking in a bowling alley"></div>
      <div class="still still-bikes" role="img" aria-label="Film still: two boys on bicycles on a leafy street"></div>
    </section>

    <footer class="credits">
      <p class="credit-line-1">HARBORLINE PICTURES <small>PRESENTS</small> “OWEN &amp; THE BLUEWATER”</p>
      <p class="credit-line-2">MILES HARPER LENA COSTA VERRI KAYLA MORROW ADDIE HOLLAND <small>AND</small> SAM WHITFIELD</p>
      <p class="credit-line-3"><small>WRITTEN AND DIRECTED BY</small> PETER ALDEN</p>
    </footer>
  </main>
</body>
</html>
```